Driving School
Brightlane Driving School
Project: Driving School
Driving School - Automotive
Creative Brief
Professional
214-52 Hollister Avenue Jamaica NY 11432
brightlanedriving@mailnest.example
www.BrightlaneDriving.example
Car & CDL Training
Calendar Or Driving school Directional MAP

```html
<!DOCTYPE html>
<html lang="en">
<head>
<meta charset="utf-8">
<title>Brightlane Driving School — Business Card</title>
<link rel="stylesheet" href="https://fonts.googleapis.com/css2?family=Montserrat:wght@500;600;800&display=swap">
<style>
  :root {
    --page-bg: #e9e9e7;
    --card-bg: #ffffff;
    --brand-blue: #2f5fa8;
    --brand-blue-dark: #1f4684;
    --brand-red: #d8262e;
    --text-grey: #5a5f66;
    --divider: #b9bdc3;
  }
  * { box-sizing: border-box; margin: 0; padding: 0; }
  html, body {
    width: 1200px; height: 914px; overflow: hidden;
    background: var(--page-bg);
    font-family: "Montserrat", sans-serif;
  }
  .business-card {
    position: absolute; left: 100px; top: 171px;
    width: 1000px; height: 572px;
    background: var(--card-bg);
    box-shadow: 0 10px 30px rgba(0,0,0,0.15);
    overflow: hidden;
  }
  .brand-mark {
    position: absolute; left: 0; right: 0; top: 110px;
    display: flex; justify-content: center; align-items: center; gap: 18px;
  }
  .brand-dot {
    width: 34px; height: 34px; border-radius: 50%;
    background: var(--brand-red);
  }
  .brand-name {
    font-weight: 800; font-size: 52px; letter-spacing: 1px;
    color: var(--brand-blue); text-transform: uppercase;
  }
  .holder {
    position: absolute; left: 170px; top: 290px; width: 330px;
    text-align: right; padding-right: 28px;
  }
  .holder-name {
    font-weight: 600; font-size: 22px; color: var(--brand-blue);
    font-variant: small-caps; letter-spacing: 2px; margin-bottom: 18px;
  }
  .holder-address {
    font-weight: 500; font-size: 15px; color: var(--text-grey);
    font-variant: small-caps; letter-spacing: 1.5px; line-height: 1.6;
  }
  .contact-divider {
    position: absolute; left: 500px; top: 285px;
    width: 2px; height: 140px; background: var(--divider);
  }
  .contact-list {
    position: absolute; left: 522px; top: 284px; list-style: none;
  }
  .contact-item {
    display: flex; align-items: center; gap: 10px;
    font-weight: 500; color: var(--text-grey);
    font-variant: small-caps; letter-spacing: 1.5px;
    height: 32px;
  }
  .contact-item.phone { font-size: 19px; }
  .contact-item.web { font-size: 13px; }
  .contact-icon {
    width: 18px; height: 18px; flex: none;
  }
  .card-bands {
    position: absolute; left: 0; bottom: 0; width: 1000px; height: 90px;
  }
</style>
</head>
<body>
  <div class="business-card">
    <div class="brand-mark">
      <span class="brand-dot"></span>
      <span class="brand-name">Brightlane Driving School</span>
    </div>

    <div class="holder">
      <p class="holder-name">Daniel Reyes</p>
      <p class="holder-address">214-52 Hollister Avenue<br>Jamaica NY 11432</p>
    </div>

    <div class="contact-divider"></div>

    <ul class="contact-list">
      <li class="contact-item phone">
        <svg class="contact-icon" viewBox="0 0 20 20"><circle cx="10" cy="10" r="10" fill="#5a5f66"/><path d="M7 5.5l1.6 2.4-1 1.1a7 7 0 0 0 3.4 3.4l1.1-1 2.4 1.6-.9 1.7c-3.9-.2-7.6-3.9-7.8-7.8z" fill="#fff"/></svg>
        718-555-0142
      </li>
      <li class="contact-item phone">
        <svg class="contact-icon" viewBox="0 0 20 20"><circle cx="10" cy="10" r="10" fill="#5a5f66"/><path d="M7 5.5l1.6 2.4-1 1.1a7 7 0 0 0 3.4 3.4l1.1-1 2.4 1.6-.9 1.7c-3.9-.2-7.6-3.9-7.8-7.8z" fill="#fff"/></svg>
        718-555-0187
      </li>
      <li class="contact-item web">
        <svg class="contact-icon" viewBox="0 0 20 20"><circle cx="10" cy="10" r="10" fill="#5a5f66"/><rect x="5" y="6.5" width="10" height="7" fill="none" stroke="#fff" stroke-width="1.3"/><path d="M5 6.5l5 4 5-4" fill="none" stroke="#fff" stroke-width="1.3"/></svg>
        brightlanedriving@mailnest.example
      </li>
      <li class="contact-item web">
        <svg class="contact-icon" viewBox="0 0 20 20"><circle cx="10" cy="10" r="10" fill="#5a5f66"/><circle cx="10" cy="10" r="5" fill="none" stroke="#fff" stroke-width="1.3"/><path d="M5 10h10M10 5c-2.5 3-2.5 7 0 10M10 5c2.5 3 2.5 7 0 10" fill="none" stroke="#fff" stroke-width="1"/></svg>
        www.BrightlaneDriving.example
      </li>
    </ul>

    <svg class="card-bands" viewBox="0 0 1000 90" preserveAspectRatio="none">
      <polygon points="0,20 640,20 632,28 0,28" fill="var(--brand-blue)"/>
      <polygon points="0,36 625,36 570,90 0,90" fill="var(--brand-blue-dark)"/>
      <polygon points="650,20 1000,20 1000,28 642,28" fill="var(--brand-red)"/>
      <polygon points="635,36 1000,36 1000,90 580,90" fill="var(--brand-red)"/>
    </svg>
  </div>
</body>
</html>
```